Jewellery company needs a biweekly flyer

Company profile:
Our company is selling jewelry directly from the factories/designers to the public. We do that cost effectively by selling through all kind of channels and therefore our prices are much lower than when that same jewelry is sold by more conventional channels like jewelry stores.

We are now in the process of developing a B to C site and want to attract potential buyers to this side by means of a (two) weekly flyer. This flyer will be distributed in a package together with all sorts of flyers from all kinds of companies and is distributed door by door being enclosed in the weekly local town newspaper.

Our products:
The jewelry we offer ranges from classic to modern pearl-, Italian silver- and gold jewelry. (Please see the examples I enclosed).

Positioning of the products:
We sell high end quality that you can wear every day or for more special occasions but no catwalk designs. You can find the more classic models that we sell in the better jewellery store but our price will be much lower.

Our customers:
Women from the age of 23 years and older
Brides of all ages

The flyer:
Format: A4– 2 sided – full color

Because it will be a (two) weekly flyer we like it to have a fixed format. This fixed format must help to recognize our flyer between all the other flyers that are distributed at the same time.

The flyer must also have a ±75% fixed layout that we every (two)week can fill with new offerings. A part of this fixed layout must be dedicated to bride jewelry.
So this part of the flyer layout is developed once and is re-used every time. Of course it is no problem if the design is made in such a way that the background need another color for every new issue.

The other ±25% of the flyer space, so in total a half A4, will be newly designed every two weeks around a theme. Like mother’s day, Christmas, winter collection, summer collection, a special bridal edition etc, etc. So every (two) weeks we need a new design that will fit in that 25% space of the flyer.
For the purpose of this contest, please take mother’s day as a theme.

The idea is that the part of the flyer that has a fixed layout will bring the recognition and the part that is redesigned every two weeks will bring the freshness of the new offering/theme and makes sure that people know that it is the new offering.

The flyers must say: These are quality products and now they are made available to you against a much better price than you expect.

Remarks:
. This flyer is for the Dutch market but we understand that, if you use text, they will be English.
. If you use a picture that we have to buy from for instance pixelmarrow.com that will be no problem
Updates

I added information in the 'must have section'. It is an attempt to explain our question better. 

Target Market(s)

Brides of all ages
We have the feeling that the buying public that we will reach with this kind of mailing is not so hip, more conservative and looking for that gain.

Industry/Entity Type

Jewelry

Requirements
Must have
• Format: A4– 2 sided – full color

Also already stated in the description but only to sum it up:

The total size of the flyer is A4 double sided.
75% of that A4 double sided space must be a fixed layout also containing a bridal section;
25% of that A4 double sided space will contain a new layout every 2 weeks and is therefore not fixed but designed every 2 weeks around a new theme.

Please contact me if I have to explain it more.

```html
<!DOCTYPE html>
<html lang="en">
<head>
<meta charset="utf-8">
<title>Lumera – Flyer, Issue January 2012</title>
<link href="https://fonts.googleapis.com/css2?family=Marcellus&family=Great+Vibes&family=PT+Sans:wght@400;700&display=swap" rel="stylesheet">
<style>
  :root {
    --berry: #8e0d45;
    --rose: #b5567a;
    --rose-soft: rgba(176, 70, 110, 0.78);
    --ink: #3a3a3a;
    --white: #ffffff;
    --stage: #ececec;
    --paper-top: #f2f0ef;
  }
  * { margin: 0; padding: 0; box-sizing: border-box; }
  html, body { width: 1200px; height: 849px; overflow: hidden; background: var(--stage); }
  body { position: relative; font-family: "PT Sans", Arial, sans-serif; }

  .page {
    position: absolute; top: 50px; width: 535px; height: 749px;
    overflow: hidden; background: var(--white);
    box-shadow: 0 2px 8px rgba(0,0,0,0.18);
  }
  .page--front { left: 46px; }
  .page--back { left: 599px; }
  .page__art { position: absolute; inset: 0; width: 535px; height: 749px; }
  .page > *:not(.page__art) { position: absolute; }

  .brand-name { font-family: "PT Sans", Arial, sans-serif; font-weight: 700; color: var(--ink); letter-spacing: 1px; line-height: 1; }
  .brand-name--masthead { left: 28px; top: 50px; font-size: 44px; }
  .brand-name--footer { left: 382px; top: 674px; font-size: 28px; }

  .issue { left: 104px; top: 102px; font-size: 9.5px; color: var(--ink); letter-spacing: 0.3px; }

  .headline { left: 70px; top: 330px; color: var(--white); font-family: "Marcellus", Georgia, serif; font-weight: 400; line-height: 1; }
  .headline__lead { display: block; font-size: 45px; }
  .headline__mid { display: block; font-size: 26px; margin-top: 4px; }
  .headline__end { display: block; font-size: 36px; margin-top: 2px; }

  .body-copy { color: var(--white); font-size: 10.2px; line-height: 1.3; }
  .body-copy--front { left: 70px; top: 476px; width: 196px; text-align: justify; }

  .caption { color: var(--white); font-size: 8px; line-height: 1.3; width: 104px; }
  .caption--bangle { left: 74px; top: 689px; }
  .caption--drops { left: 281px; top: 662px; }
  .caption--chain { left: 410px; top: 604px; }

  .section-title { color: var(--white); font-family: "Marcellus", Georgia, serif; font-weight: 400; font-size: 21px; line-height: 1; }
  .section-title--wedding { left: 199px; top: 192px; }
  .section-title--offer { left: 263px; top: 365px; }
  .body-copy--wedding { left: 199px; top: 226px; width: 312px; font-size: 7.6px; }
  .body-copy--offer { left: 263px; top: 399px; width: 204px; font-size: 7.6px; text-align: justify; }

  .theme-title { left: 17px; top: 383px; font-family: "Great Vibes", cursive; font-size: 31px; color: var(--berry); }
  .web-address { left: 43px; top: 707px; font-size: 15px; font-weight: 700; color: var(--ink); }
</style>
</head>
<body>

<section class="page page--front">
  <svg class="page__art" viewBox="0 0 535 749">
    <defs>
      <linearGradient id="portraitTone" x1="0" y1="0" x2="1" y2="1">
        <stop offset="0" stop-color="#5a4a45"/>
        <stop offset="0.45" stop-color="#b98a76"/>
        <stop offset="1" stop-color="#3c2a28"/>
      </linearGradient>
      <radialGradient id="itemTone" cx="0.5" cy="0.5" r="0.6">
        <stop offset="0" stop-color="#ffffff"/>
        <stop offset="1" stop-color="#d9d6d4"/>
      </radialGradient>
    </defs>
    <rect role="img" aria-label="Photo of a woman wearing a silver necklace, drop earrings and a crystal heart pendant" x="0" y="0" width="535" height="749" fill="url(#portraitTone)"/>
    <path class="masthead-band" d="M0,0 H535 V98 C380,100 150,130 0,190 Z" fill="var(--paper-top)" opacity="0.95"/>
    <path class="offer-swoop" d="M535,322 C520,520 390,655 0,688 V749 H535 Z" fill="var(--berry)"/>

    <circle cx="189" cy="642" r="54" fill="var(--white)" stroke="var(--berry)" stroke-width="7"/>
    <circle role="img" aria-label="Gold bead bangle" cx="189" cy="642" r="44" fill="url(#itemTone)"/>
    <circle cx="314" cy="602" r="52" fill="var(--white)" stroke="var(--berry)" stroke-width="7"/>
    <circle role="img" aria-label="Smoky quartz drop earrings" cx="314" cy="602" r="42" fill="url(#itemTone)"/>
    <circle cx="434" cy="539" r="52" fill="var(--white)" stroke="var(--berry)" stroke-width="7"/>
    <circle role="img" aria-label="Silver link necklace" cx="434" cy="539" r="42" fill="url(#itemTone)"/>
  </svg>

  <p class="brand-name brand-name--masthead">LUMERA</p>
  <p class="issue">ISSUE JANUARY 2012</p>

  <h1 class="headline">
    <span class="headline__lead">Quality products</span>
    <span class="headline__mid">avalailable at a much</span>
    <span class="headline__end">better price</span>
  </h1>

  <p class="body-copy body-copy--front">Every piece comes straight from the workshops and designers we trust, so you wear fine pearl, silver and gold for far less than shop prices. Classic lines, honest quality and no catwalk fuss. Visit our new web shop and see this issue's finest choices at prices you did not expect.</p>

  <p class="caption caption--bangle">Gold bead bangle with fine silver links and clasp.</p>
  <p class="caption caption--drops">Smoky quartz drop earrings on rose gold chains, light and easy to wear every day.</p>
  <p class="caption caption--chain">Italian silver link necklace with polished oval rings, a timeless daily piece.</p>
</section>

<section class="page page--back">
  <svg class="page__art" viewBox="0 0 535 749">
    <defs>
      <linearGradient id="bridalTone" x1="0" y1="0" x2="1" y2="0.6">
        <stop offset="0" stop-color="#c9d7b8"/>
        <stop offset="0.5" stop-color="#f3ecea"/>
        <stop offset="1" stop-color="#e8c9cf"/>
      </linearGradient>
      <linearGradient id="bouquetTone" x1="0" y1="0" x2="0.6" y2="1">
        <stop offset="0" stop-color="#f4d8dc"/>
        <stop offset="0.6" stop-color="#f7e9e6"/>
        <stop offset="1" stop-color="#b9cfa8"/>
      </linearGradient>
      <radialGradient id="ringTone" cx="0.5" cy="0.45" r="0.6">
        <stop offset="0" stop-color="#ffffff"/>
        <stop offset="1" stop-color="#cfcac8"/>
      </radialGradient>
    </defs>

    <rect role="img" aria-label="Soft-focus photo of wedding flowers and rings" x="0" y="0" width="535" height="340" fill="url(#bridalTone)"/>
    <path class="wedding-panel" d="M0,205 C40,190 90,175 125,165 C150,95 250,60 330,65 L535,40 V335 C400,305 200,318 0,340 Z" fill="var(--rose-soft)"/>

    <circle cx="78" cy="224" r="57" fill="var(--white)" stroke="var(--rose)" stroke-width="8"/>
    <circle role="img" aria-label="Gold wedding bands on a white rose" cx="78" cy="224" r="49" fill="url(#ringTone)"/>
    <circle cx="176" cy="124" r="58" fill="var(--white)" stroke="var(--rose)" stroke-width="8"/>
    <circle role="img" aria-label="Pair of silver wedding bands" cx="176" cy="124" r="50" fill="url(#ringTone)"/>
    <circle cx="305" cy="80" r="57" fill="var(--white)" stroke="var(--rose)" stroke-width="8"/>
    <circle role="img" aria-label="White gold diamond engagement rings" cx="305" cy="80" r="49" fill="url(#ringTone)"/>
    <circle cx="445" cy="74" r="57" fill="var(--white)" stroke="var(--rose)" stroke-width="8"/>
    <circle role="img" aria-label="Yellow gold solitaire ring" cx="445" cy="74" r="49" fill="url(#ringTone)"/>

    <rect role="img" aria-label="Bouquet of pink and white carnations" x="0" y="325" width="240" height="370" fill="url(#bouquetTone)"/>
    <path class="theme-panel" fill-rule="evenodd" fill="var(--berry)"
      d="M0,332 C150,312 350,300 535,292 V505 C470,592 360,632 250,642 L119,614 C70,560 12,505 0,472 Z
         M119,600 C60,540 8,480 10,420 C12,370 60,345 100,360 C112,365 118,375 121,385 C126,365 150,345 185,345 C225,345 240,380 235,420 C230,490 170,550 119,600 Z"/>

    <circle cx="450" cy="532" r="50" fill="var(--white)" stroke="#f1ecee" stroke-width="3"/>
    <circle role="img" aria-label="Multi-strand black pearl necklace" cx="450" cy="532" r="42" fill="url(#ringTone)"/>
    <circle cx="325" cy="643" r="50" fill="var(--white)" stroke="#f1ecee" stroke-width="3"/>
    <circle role="img" aria-label="Pearl bracelet with red stone" cx="325" cy="643" r="42" fill="url(#ringTone)"/>
    <circle cx="188" cy="653" r="54" fill="var(--white)" stroke="#f1ecee" stroke-width="3"/>
    <circle role="img" aria-label="Single strand pearl necklace on a display bust" cx="188" cy="653" r="46" fill="url(#ringTone)"/>
  </svg>

  <h2 class="section-title section-title--wedding">Wedding corner</h2>
  <p class="body-copy body-copy--wedding">Find the perfect rings for your big day. Our bridal pieces come from the same makers that supply the finest jewellery stores, set in white and yellow gold with brilliant stones, and all at a price that leaves more room in your wedding budget. Come and see the full bridal range online.</p>

  <p class="theme-title">Mother's day</p>

  <h2 class="section-title section-title--offer">Special offer</h2>
  <p class="body-copy body-copy--offer">Spoil your mother with pearls this year. Our freshwater strands, bracelets and necklaces are made for her everyday moments and special days alike. For a limited time every pearl piece in this issue comes at an even sharper price. Order online before the day and we wrap it as a gift for free.</p>

  <p class="web-address">www.lumerajewels.eu</p>
  <p class="brand-name brand-name--footer">LUMERA</p>
</section>

</body>
</html>
```